Business Card Design Project

I want a design for my business cards based on an excisting logo design.

Target Market(s)

Marketeers, PR-peeps, CEO's, decisionmakers, entrepreneurs

Industry/Entity Type

Business

Requirements
Nice to have
• Some visual interest on the back too
Should not have
• Sarif on the font

```html
<!DOCTYPE html>
<html lang="nl">
<head>
<meta charset="utf-8">
<title>FernLoop PR – visitekaartjes</title>
<link rel="stylesheet" href="https://fonts.googleapis.com/css2?family=Source+Sans+3:wght@400;600;700&display=swap">
<style>
  :root {
    --green: #0b8a3e;
    --lime: #8cc63f;
    --grey: #6d6e70;
    --card: #f4f5f5;
    --stage: #e8e5e0;
    --white: #ffffff;
  }
  * { box-sizing: border-box; margin: 0; padding: 0; }
  html, body {
    width: 1200px; height: 880px; overflow: hidden;
    background: var(--stage);
    font-family: "Source Sans 3", sans-serif;
  }
  .sheet {
    width: 1200px; height: 880px;
    display: flex; align-items: center; justify-content: center; gap: 40px;
  }
  .card {
    position: relative;
    width: 540px; height: 320px;
    background: var(--card);
    overflow: hidden;
    box-shadow: 0 6px 18px rgba(0,0,0,.18);
  }
  .card-bands { position: absolute; inset: 0; width: 100%; height: 100%; }

  /* Front */
  .front-brand {
    position: absolute; left: 0; right: 0; top: 34px;
    display: flex; flex-direction: column; align-items: center; gap: 16px;
  }
  .brand-dot {
    width: 104px; height: 104px; border-radius: 50%;
    background: var(--lime);
  }
  .brand-name {
    color: var(--grey); font-weight: 400; font-size: 40px; letter-spacing: 1px; line-height: 1;
  }
  .tagline {
    position: absolute; left: 28px; bottom: 14px;
    color: var(--white); font-size: 14.5px; font-weight: 400;
  }

  /* Back */
  .back-brand {
    position: absolute; left: 26px; top: 18px;
    display: flex; align-items: center; gap: 16px;
  }
  .back-brand .brand-dot { width: 52px; height: 52px; }
  .back-brand .brand-name { font-size: 34px; }
  .holder {
    position: absolute; left: 58px; top: 100px;
    color: var(--white); font-weight: 700; font-size: 21px;
  }
  .website {
    position: absolute; left: 30px; top: 208px;
    color: var(--white); font-size: 13.5px;
  }
  .divider {
    position: absolute; left: 226px; top: 176px; width: 1px; height: 124px;
    background: rgba(255,255,255,.75);
  }
  .contact-list {
    position: absolute; left: 240px; top: 182px; list-style: none;
    color: var(--white); font-size: 13.5px; line-height: 23px;
  }
  .contact-list li { display: flex; align-items: center; gap: 8px; }
  .contact-icon { width: 12px; height: 12px; flex: none; fill: var(--white); }
  .social-mark { width: 11px; height: 11px; background: var(--white); flex: none; }
</style>
</head>
<body>
<main class="sheet">

  <section class="card card-front" aria-label="Voorkant visitekaartje">
    <svg class="card-bands" viewBox="0 0 540 320" preserveAspectRatio="none" aria-hidden="true">
      <path d="M0,202 Q300,226 540,236 L540,256 Q270,244 0,212 Z" fill="var(--lime)"/>
      <path d="M0,210 Q290,240 540,252 L540,320 L0,320 Z" fill="var(--green)"/>
    </svg>
    <div class="front-brand">
      <span class="brand-dot"></span>
      <span class="brand-name">FernLoop PR</span>
    </div>
    <p class="tagline">Systemisch en strategisch PR-, marketing- en communicatieadvies</p>
  </section>

  <section class="card card-back" aria-label="Achterkant visitekaartje">
    <svg class="card-bands" viewBox="0 0 540 320" preserveAspectRatio="none" aria-hidden="true">
      <path d="M0,70 C200,78 400,125 540,172 L540,192 C400,145 200,92 0,82 Z" fill="var(--lime)"/>
      <path d="M0,80 C200,90 400,140 540,190 L540,320 L0,320 Z" fill="var(--green)"/>
      <path d="M0,100 L14,110 L0,120 Z" fill="var(--lime)"/>
    </svg>
    <div class="back-brand">
      <span class="brand-dot"></span>
      <span class="brand-name">FernLoop PR</span>
    </div>
    <p class="holder">Lotte Brandsma</p>
    <p class="website">www.fernlooppr.nl</p>
    <span class="divider"></span>
    <ul class="contact-list">
      <li>
        <svg class="contact-icon" viewBox="0 0 12 12" aria-hidden="true"><path d="M6,1 L11.5,6 L10,6 L10,11 L7.2,11 L7.2,8 L4.8,8 L4.8,11 L2,11 L2,6 L0.5,6 Z"/></svg>
        Lindelaan 48, 6711 AB Ede
      </li>
      <li>
        <svg class="contact-icon" viewBox="0 0 12 12" aria-hidden="true"><path d="M3,0.5 H9 A1,1 0 0 1 10,1.5 V10.5 A1,1 0 0 1 9,11.5 H3 A1,1 0 0 1 2,10.5 V1.5 A1,1 0 0 1 3,0.5 Z M3.5,2 V8 H8.5 V2 Z"/></svg>
        +31(0)6 12345678
      </li>
      <li>
        <svg class="contact-icon" viewBox="0 0 12 12" aria-hidden="true"><path d="M0.5,2.5 H11.5 V9.5 H0.5 Z M1.5,3.3 L6,6.8 L10.5,3.3" stroke="var(--green)" stroke-width="0.9"/></svg>
        lotte.brandsma@fernlooppr.nl
      </li>
      <li><span class="social-mark"></span>chirpnet.nl/_fernlooppr</li>
      <li><span class="social-mark"></span>kringboek.nl/fernlooppr</li>
    </ul>
  </section>

</main>
</body>
</html>
```